Simple menu needed for Asian food truck

We are an Asian food truck that attends big festivals. Our menu is very simple featuring only about 5 or 6 dishes, but we need big pictures and lettering to capture the attention of festival goers. Our motto is "Fresh, Authentic, Homemade", it would be great to include that somewhere. We also need a menu that possibly magnetic so that we can easily take off items that are sold out, change pricing or add different dishes for specific venues. Attached is an example of what our current menu looks like.

```html
<!DOCTYPE html>
<html lang="en">
<head>
<meta charset="utf-8">
<title>Tam's Authentic Egg Rolls – Menu</title>
<link rel="stylesheet" href="https://fonts.googleapis.com/css2?family=Bebas+Neue&family=Oswald:wght@300;400&family=Roboto+Condensed:wght@400;700&display=swap">
<style>
  :root {
    --cream: #fcf6e4;
    --slate: #1e2126;
    --slate-light: #33373d;
    --gold: #f4c04e;
    --gold-deep: #e6a93a;
    --orange: #d8772a;
    --price-yellow: #f6c44b;
    --ink: #3a3a3a;
    --white: #ffffff;
  }
  * { box-sizing: border-box; margin: 0; padding: 0; }
  html, body { width: 972px; height: 1200px; overflow: hidden; background: var(--cream); }
  .menu { position: relative; width: 972px; height: 1200px; background: var(--cream); overflow: hidden; font-family: "Roboto Condensed", sans-serif; }
  .menu-backdrop { position: absolute; inset: 0; width: 972px; height: 1200px; }
  .menu-title {
    position: absolute; left: 43px; top: 36px;
    font-family: "Oswald", sans-serif; font-weight: 400; font-size: 40px;
    letter-spacing: 0.5px; color: var(--ink);
  }
  .brand { position: absolute; left: 640px; top: 70px; display: flex; align-items: center; gap: 12px; }
  .brand-dot { width: 34px; height: 34px; border-radius: 50%; background: var(--orange); }
  .brand-name { font-family: "Bebas Neue", sans-serif; font-size: 44px; color: var(--orange); line-height: 1; }

  .dishes {
    position: absolute; left: 16px; top: 236px; width: 940px;
    display: grid; grid-template-columns: repeat(3, 310px); grid-template-rows: 432px 432px; column-gap: 5px;
  }
  .dish { position: relative; text-align: center; color: var(--white); }
  .dish-art { position: relative; height: 292px; }
  .dish-blob { position: absolute; left: 40px; top: 0; width: 230px; height: 270px; }
  .dish-photo {
    position: absolute; left: 10px; top: 60px; width: 290px; height: 160px; border-radius: 14px;
  }
  .dish-photo--eggrolls { background: linear-gradient(135deg, #f2f2ef 0%, #e0b46a 40%, #c98a3d 70%, #f4f2ee 100%); transform: rotate(-6deg); }
  .dish-photo--angelwing { background: linear-gradient(90deg, #f4f4f2 0%, #c9a76a 30%, #e9b24f 70%, #f4f4f2 100%); top: 80px; height: 130px; }
  .dish-photo--springrolls { background: linear-gradient(135deg, #f3f3f0 0%, #e9d9cf 35%, #f0a08a 60%, #f3f3f0 100%); transform: rotate(-4deg); }
  .dish-photo--bbq { background: linear-gradient(160deg, #f4f4f2 0%, #9e3434 35%, #6e1f24 65%, #f4f4f2 100%); top: 70px; height: 140px; }
  .dish-photo--tea { left: 70px; width: 190px; top: 20px; height: 220px; background: linear-gradient(90deg, #e5553f 0%, #f7a33a 50%, #f4c551 100%); border-radius: 10px 10px 24px 24px; }
  .dish-photo--rice { background: linear-gradient(135deg, #f4f4f2 0%, #d8c08b 35%, #b88a50 65%, #f4f4f2 100%); transform: rotate(-3deg); }

  .price-badge {
    position: absolute; left: 196px; top: 184px; width: 92px; height: 92px; border-radius: 50%;
    background: var(--orange); border: 3px solid var(--cream);
    display: flex; flex-direction: column; align-items: center; justify-content: center; color: var(--white);
  }
  .price-amount { font-family: "Bebas Neue", sans-serif; font-size: 48px; line-height: 0.9; }
  .price-note { font-family: "Bebas Neue", sans-serif; font-size: 14px; letter-spacing: 0.3px; }

  .dish-name { font-family: "Bebas Neue", sans-serif; font-weight: 400; font-size: 37px; line-height: 1; margin-top: 12px; letter-spacing: 0.5px; }
  .dish-detail { font-size: 16px; line-height: 1.3; margin-top: 6px; }
  .dish-deal { font-family: "Bebas Neue", sans-serif; font-size: 24px; color: var(--price-yellow); margin-top: 8px; letter-spacing: 0.5px; }

  .social { position: absolute; left: 36px; top: 1092px; display: flex; gap: 14px; }
  .social-link { display: flex; align-items: center; gap: 4px; font-size: 13px; color: var(--orange); }
  .social-link::before { content: ""; width: 12px; height: 12px; border-radius: 50%; border: 1.5px solid var(--orange); }
  .payments { position: absolute; left: 32px; top: 1146px; display: flex; gap: 6px; }
  .payment-card {
    width: 60px; height: 36px; border-radius: 3px; background: var(--white); border: 1px solid #d6d2c6;
    display: flex; align-items: center; justify-content: center;
    font-size: 11px; font-weight: 700; color: var(--ink);
  }
</style>
</head>
<body>
<main class="menu">
  <svg class="menu-backdrop" viewBox="0 0 972 1200" aria-hidden="true">
    <defs>
      <radialGradient id="slate-texture" cx="50%" cy="45%" r="70%">
        <stop offset="0" stop-color="#383c42"/>
        <stop offset="1" stop-color="#1a1d21"/>
      </radialGradient>
    </defs>
    <path fill="url(#slate-texture)" d="M0,140 C80,70 230,80 330,120 C430,160 480,112 560,132 C650,152 700,225 800,228 C880,230 925,188 972,178 L972,1200 L873,1200 C850,1150 820,1125 770,1122 C700,1118 650,1125 600,1108 C540,1088 500,1130 440,1098 C380,1066 330,1090 260,1094 C180,1098 120,1050 0,1050 Z"/>
  </svg>

  <h1 class="menu-title">TAM'S AUTHENTIC EGG ROLLS</h1>
  <div class="brand"><span class="brand-dot"></span><span class="brand-name">Tam's Egg Rolls</span></div>

  <section class="dishes">
    <article class="dish">
      <div class="dish-art">
        <svg class="dish-blob" viewBox="0 0 230 270" aria-hidden="true"><path fill="var(--gold)" d="M110,8 C175,0 225,50 222,130 C220,200 190,262 120,262 C50,262 8,215 10,140 C12,70 50,14 110,8 Z"/></svg>
        <div class="dish-photo dish-photo--eggrolls" role="img" aria-label="Three golden fried chicken egg rolls on a white paper tray"></div>
        <div class="price-badge"><span class="price-amount">$6</span><span class="price-note">3 FOR $6</span></div>
      </div>
      <h2 class="dish-name">Chicken Eggrolls</h2>
      <p class="dish-deal">3 for $6</p>
    </article>

    <article class="dish">
      <div class="dish-art">
        <svg class="dish-blob" viewBox="0 0 230 270" aria-hidden="true"><path fill="var(--gold)" d="M120,5 C185,5 220,60 215,135 C210,210 175,265 110,262 C45,258 12,205 15,130 C18,60 60,5 120,5 Z"/></svg>
        <div class="dish-photo dish-photo--angelwing" role="img" aria-label="Stuffed fried chicken wing with fried rice on a white plate"></div>
        <div class="price-badge"><span class="price-amount">$8</span><span class="price-note">COMBO</span></div>
      </div>
      <h2 class="dish-name">Angel Wing</h2>
      <p class="dish-detail">(Stuffed Chicken Wing)<br>with side of fried rice</p>
    </article>

    <article class="dish">
      <div class="dish-art">
        <svg class="dish-blob" viewBox="0 0 230 270" aria-hidden="true"><path fill="var(--gold)" d="M115,6 C180,8 224,55 220,135 C216,205 180,262 112,260 C45,258 10,210 12,135 C14,65 55,4 115,6 Z"/></svg>
        <div class="dish-photo dish-photo--springrolls" role="img" aria-label="Two fresh rice paper spring rolls with shrimp on a white tray"></div>
        <div class="price-badge"><span class="price-amount">$6</span><span class="price-note">2 FOR $6</span></div>
      </div>
      <h2 class="dish-name">Fresh Springrolls</h2>
      <p class="dish-detail">(Shrimp or Veggie)</p>
      <p class="dish-deal">2 for $6</p>
    </article>

    <article class="dish">
      <div class="dish-art">
        <svg class="dish-blob" viewBox="0 0 230 270" aria-hidden="true"><path fill="var(--gold)" d="M105,10 C170,2 222,55 220,135 C218,205 180,262 115,262 C50,262 10,210 12,135 C14,70 45,18 105,10 Z"/></svg>
        <div class="dish-photo dish-photo--bbq" role="img" aria-label="Two Chinese barbecue pork skewers on a white paper tray"></div>
        <div class="price-badge"><span class="price-amount">$6</span><span class="price-note">2 FOR $6</span></div>
      </div>
      <h2 class="dish-name">Chinese BBQ Pork</h2>
      <p class="dish-detail">Skewers</p>
      <p class="dish-deal" style="margin-top:0">2 for $6</p>
    </article>

    <article class="dish">
      <div class="dish-art">
        <svg class="dish-blob" viewBox="0 0 230 270" aria-hidden="true"><path fill="var(--gold)" d="M118,4 C182,6 222,58 218,132 C214,205 178,264 112,262 C46,260 12,208 14,134 C16,64 56,2 118,4 Z"/></svg>
        <div class="dish-photo dish-photo--tea" role="img" aria-label="Three glasses of strawberry, mango and peach iced tea with straws"></div>
        <div class="price-badge"><span class="price-amount">$5</span><span class="price-note">GLASS</span></div>
      </div>
      <h2 class="dish-name">Flavored Tea</h2>
      <p class="dish-detail">Strawberry, Mango<br>or Peach</p>
    </article>

    <article class="dish">
      <div class="dish-art">
        <svg class="dish-blob" viewBox="0 0 230 270" aria-hidden="true"><path fill="var(--gold)" d="M112,6 C178,4 222,56 220,132 C218,204 182,262 114,262 C48,262 10,210 12,134 C14,66 50,8 112,6 Z"/></svg>
        <div class="dish-photo dish-photo--rice" role="img" aria-label="Fried rice with pork, peas and carrots in a paper boat tray"></div>
        <div class="price-badge"><span class="price-amount">$5</span><span class="price-note">BOWL</span></div>
      </div>
      <h2 class="dish-name">Fried Rice</h2>
      <p class="dish-detail">(Chicken or Pork)</p>
    </article>
  </section>

  <nav class="social">
    <span class="social-link">Friendly</span>
    <span class="social-link">Chirper</span>
    <span class="social-link">Snapgram</span>
  </nav>
  <div class="payments">
    <span class="payment-card">Vela</span>
    <span class="payment-card">Meridian</span>
    <span class="payment-card">Amber Card</span>
    <span class="payment-card">Dawnpay</span>
  </div>
</main>
</body>
</html>
```